Manufacturing Company WordPress Website Design

Looking for a modern WordPress design for a manufacturer of oil separation and coolant recycling products called BrightFloe. This is a business-to-business marketer in the industrial manufacturing sector. BrightFloe sells to CNC manufacturing companies and their products are known as some of the best tools in the world for skimming and separating floating oils, metallic fines, and other contaminants from industrial process fluids.

The winning design will be based on a responsive WP theme. Include the theme name if your design is selected by the client. Provide Home, Product and Case Study page views with your submission.

THE BRIGHTFLOE BRAND
The BrightFloe brand is all about connection and partnership. They are down-to-earth, relatable, helpful and fun to hang out with. The brand voice is humble, authentic and helpful and they are driven by connection, togetherness and inclusion.

The BrightFloe target audience is plant managers, enterprise engineers and business owners in CNC machining manufacturing companies across a variety of industries (automotive, aerospace, energy, medical and transportation).

BrightFloe is looking for a clean, modern website that better represents their brand with a more polished and professional design. It should be:
- responsive and mobile-friendly
- easily findable for key search criteria
- a source for improved lead generation for prospective sales
- more easily editable

A design that is oriented toward these goals will be selected as the winner.

The winning designer may be chosen to code the website, or to code the initial pages in the concept design.

Current Website:
https://brightfloe-example.com/index.html

Competitors:
https://www.kelvora-example.com/
https://www.tundix-example.com/
https://www.voltarin-example.com/

Sites We Like:
https://northgateweldworks-example.com/
- we like the clean layout of the home page in a grid-like design, simple header and footer, the parallax scrolling, and the mobile responsiveness.

https://www.kelvora-example.com/fluid-filtration/sentinel-coolant-recycling-systems/
- we like the way the content is presented on the Kelvora product page - specifically, we like the use of the tabs below the main product images to present a lot of content without it looking overwhelmingly busy.

https://pinecrestpanes-example.com/healthcare/harborview-care-clinic/
- we like the way Pinecrest Panes presents their cases studies with a combination of useful information highlighted by informative icons and pictures to present key statistics in the case study. We would like the BrightFloe case studies to almost feel like an infographic presentation on the website.

Attached files to help your designs:
- Brand Identity Guidelines
- BrightFloe Logos
- Product Photos
- Brand Photos
- Home page content
- Coolant Recycling product page content
- Case Study page content
- Site Map
- Wire Frames

Target Market(s)

Industry/Entity Type

Industrial

Coding

Coded - Design and coding required

Number of Pages Required

3 page

Font styles to use
Sans Serif
Other font styles liked:
• DINPro is used on all collateral - see brand guidelines

Requirements
Must have
• See the brand guidelines file attached for colors and logo usage

```html
<!DOCTYPE html>
<html lang="en">
<head>
<meta charset="utf-8">
<title>BrightFloe — Oil Separation &amp; Coolant Recycling Systems</title>
<link href="https://fonts.googleapis.com/css2?family=Barlow:ital,wght@0,400;0,500;0,600;0,700;0,800;1,400;1,500;1,600&family=Kaushan+Script&display=swap" rel="stylesheet">
<style>
:root{
  --navy:#15306b;
  --navy-deep:#0d1f4a;
  --red:#d3202b;
  --red-deep:#a8141d;
  --ink:#1d2433;
  --text:#4a5162;
  --grey-bg:#eef0f3;
  --white:#ffffff;
  --footer:#161a24;
}
*{margin:0;padding:0;box-sizing:border-box}
html,body{width:1200px;height:3876px;overflow:hidden}
body{font-family:"Barlow",Arial,sans-serif;color:var(--text);background:var(--white);position:relative}
.section{position:absolute;left:0;width:1200px;overflow:hidden}
a{color:inherit;text-decoration:none}

/* header + hero */
.hero{top:0;height:790px}
.hero-bg{position:absolute;inset:0;background:linear-gradient(100deg,#1b2f5e 0%,#3b5180 35%,#7d8aa6 62%,#a4acbd 100%)}
.hero-person{position:absolute;right:80px;top:90px;width:430px;height:640px;background:linear-gradient(160deg,#c98a3a 0%,#6a5a4e 45%,#2c3553 100%);opacity:.75;border-radius:6px}
.hero-shade{position:absolute;inset:0;background:linear-gradient(90deg,rgba(13,31,74,.75) 0%,rgba(13,31,74,.35) 55%,rgba(13,31,74,0) 100%)}
.brand{position:absolute;left:40px;top:14px;display:flex;align-items:center;gap:12px;color:var(--white)}
.brand-dot{width:44px;height:44px;border-radius:50%;background:var(--white);flex:none}
.brand-name{font-size:30px;font-weight:700;letter-spacing:.3px;white-space:nowrap}
.brand-tag{position:absolute;left:96px;top:54px;font-size:9px;color:#d9deea;letter-spacing:.4px}
.contact-pills{position:absolute;left:520px;top:14px;display:flex;gap:12px}
.pill{display:flex;align-items:center;gap:6px;background:var(--white);border-radius:14px;padding:5px 14px;font-size:12px;color:var(--ink);white-space:nowrap}
.pill svg{width:12px;height:12px}
.estimate{position:absolute;right:0;top:0;width:98px;height:56px;background:var(--red);color:var(--white);font-size:11px;font-weight:600;text-align:center;padding-top:14px;line-height:1.25}
.main-nav{position:absolute;left:470px;top:60px;width:730px;height:42px;background:var(--navy-deep);display:flex}
.main-nav a{flex:1;color:var(--white);font-size:14px;font-weight:500;display:flex;align-items:center;justify-content:center;border-right:1px solid rgba(255,255,255,.15);white-space:nowrap}
.main-nav a.current{background:var(--red)}
.hero-title{position:absolute;left:80px;top:262px;font-size:46px;font-weight:800;line-height:1.05;text-transform:uppercase;color:var(--red);width:680px}
.hero-title span{color:var(--white)}
.hero-lead{position:absolute;left:80px;top:368px;width:380px;font-size:13px;line-height:1.45;color:#e2e6ef}
.hero-actions{position:absolute;left:80px;top:438px;display:flex;gap:22px}
.btn{display:flex;align-items:center;gap:10px;height:38px;padding:0 20px;font-size:12px;font-weight:700;letter-spacing:.5px;text-transform:uppercase;color:var(--white);white-space:nowrap}
.btn-red{background:var(--red)}
.btn-navy{background:var(--navy)}
.btn svg{width:12px;height:12px;flex:none}
.hero-wave{position:absolute;left:0;bottom:0;width:1200px;height:110px}

/* about */
.about{top:790px;height:350px}
.about-visual{position:absolute;left:120px;top:20px;width:320px;height:300px;border-radius:6px;background:linear-gradient(145deg,#dfe4ee 0%,#b9c3d8 50%,#8c9bbb 100%)}
.section-title{font-size:32px;font-weight:800;color:var(--navy);text-transform:uppercase;letter-spacing:.3px;position:relative;padding-bottom:12px}
.section-title::after{content:"";position:absolute;left:0;bottom:0;width:54px;height:3px;background:var(--red)}
.about-text{position:absolute;left:570px;top:60px;width:560px}
.body-copy{font-size:13px;line-height:1.6;color:var(--text);margin-top:16px}
.learn{display:inline-flex;align-items:center;gap:10px;margin-top:16px;font-size:12px;font-weight:700;color:var(--navy);text-transform:uppercase;letter-spacing:.5px}
.learn svg{width:12px;height:12px}

/* products */
.product.tint{background:linear-gradient(90deg,#eceef2 0%,#f6f7f9 60%,#e7e9ee 100%)}
.oil{top:1140px;height:290px}
.coolant{top:1430px;height:290px}
.magnetic{top:1720px;height:310px}
.product-text{position:absolute;width:470px}
.product-title{font-size:27px;font-weight:800;color:var(--navy);text-transform:uppercase}
.product-img{position:absolute;border-radius:4px}
.oil .product-text{left:155px;top:78px}
.oil .product-img{left:690px;top:44px;width:280px;height:210px;background:linear-gradient(180deg,#c4c9d2,#6a7384)}
.coolant .product-text{left:525px;top:88px}
.coolant .product-img{left:150px;top:30px;width:300px;height:230px;background:linear-gradient(180deg,#4171c4 0%,#1c3f8a 70%,#555 100%)}
.magnetic .product-text{left:155px;top:80px}
.magnetic .product-img{left:720px;top:30px;width:460px;height:250px;background:linear-gradient(90deg,rgba(238,240,243,0),#c6cad2 45%,#8c939f 100%);opacity:.6}

/* trusted */
.trusted{top:2030px;height:380px}
.trusted-title{position:absolute;left:0;width:1200px;top:110px;text-align:center;font-size:32px;font-weight:800;color:var(--navy);text-transform:uppercase}
.logo-row{position:absolute;left:70px;top:230px;width:1060px;display:flex;align-items:center;justify-content:space-between}
.logo-row svg.arrow{width:22px;height:22px}
.client{font-size:22px;font-weight:700;color:var(--navy);display:flex;align-items:center;gap:8px;white-space:nowrap}
.client i{display:block;width:14px;height:14px;background:var(--navy)}

/* roi */
.roi{top:2410px;height:570px}
.roi-bands{position:absolute;left:0;top:0;width:1200px;height:570px}
.roi-left{position:absolute;left:170px;top:110px;width:420px;color:var(--white)}
.roi-brand{display:flex;align-items:center;gap:10px}
.roi-brand .brand-dot{width:40px;height:40px}
.roi-copy{margin-top:38px;font-size:19px;font-style:italic;line-height:1.45;font-weight:500}
.roi-left .btn{margin-top:30px;width:max-content}
.roi-panel{position:absolute;left:600px;top:60px;width:600px;height:470px;background:linear-gradient(135deg,#35507f,#1e3260 60%,#2e4877)}
.roi-heading{position:absolute;left:0;width:600px;top:46px;text-align:center;font-family:"Kaushan Script",cursive;font-size:38px;color:var(--white)}
.slider{position:absolute;left:80px;width:430px}
.slider-label{font-size:10px;color:#dfe4ee;text-align:center;margin-bottom:10px}
.slider-row{display:flex;align-items:center;gap:12px}
.slider-row b{font-size:13px;color:var(--white);font-weight:600;width:30px}
.slider-track{position:relative;flex:1;height:4px;background:rgba(255,255,255,.75);border-radius:2px}
.slider-fill{position:absolute;left:0;top:0;height:4px;background:var(--red);border-radius:2px}
.slider-knob{position:absolute;top:-6px;width:16px;height:16px;border-radius:50%;background:var(--white);border:3px solid var(--red)}

/* case studies */
.cases{top:2980px;height:430px}
.cases-title{position:absolute;left:0;width:1200px;top:60px;text-align:center;font-size:27px;font-weight:800;color:var(--navy);text-transform:uppercase}
.case-row{position:absolute;left:60px;top:150px;width:1080px;display:flex;align-items:center;justify-content:space-between}
.case-row svg.arrow{width:22px;height:22px}
.case-card{width:230px;height:210px;background:var(--white);box-shadow:0 4px 18px rgba(20,30,60,.14);padding:22px 18px}
.case-card p{font-size:10px;line-height:1.5;color:var(--text)}
.case-badge{margin:22px auto 0;width:120px;height:44px;border-radius:22px;background:var(--red)}
.case-lines{margin-top:16px}
.case-lines span{display:block;height:3px;background:#d8dce3;margin:6px auto;width:150px}

/* newsletter */
.newsletter{top:3410px;height:230px;background:linear-gradient(180deg,#2a2f3b,#1b1f29)}
.news-title{position:absolute;left:0;width:1200px;top:62px;text-align:center;font-size:27px;font-weight:800;color:var(--white);text-transform:uppercase}
.news-form{position:absolute;left:280px;top:130px;width:640px;height:42px;display:flex;border:2px solid var(--red);background:var(--white)}
.news-form .field{flex:1;font-size:12px;color:#8b91a0;display:flex;align-items:center;gap:8px;padding-left:14px}
.news-form .field svg{width:14px;height:14px}
.news-form .submit{width:140px;background:var(--red);color:var(--white);font-size:13px;font-weight:600;display:flex;align-items:center;justify-content:center}

/* footer */
.footer{top:3640px;height:236px;background:var(--footer);color:#c9ccd4}
.footer-brand{position:absolute;left:60px;top:28px;width:270px}
.footer-brand .brand-row{display:flex;align-items:center;gap:10px;color:var(--white)}
.footer-brand .brand-dot{width:34px;height:34px}
.footer-brand .brand-name{font-size:22px}
.footer-brand p{font-size:9.5px;line-height:1.5;margin-top:12px;color:#a9adb8}
.footer-col{position:absolute;top:34px}
.footer-col h4{font-size:19px;font-weight:600;color:var(--white);margin-bottom:12px}
.footer-col li{list-style:none;font-size:11px;line-height:1.75;color:#c1c4cc;white-space:nowrap}
.footer-col .contact-line{display:flex;align-items:center;gap:8px}
.footer-col .contact-line svg{width:11px;height:11px}
.social{display:flex;gap:8px}
.social i{display:block;width:16px;height:16px;border-radius:50%;background:#c9ccd4}
.copyright{position:absolute;left:0;bottom:0;width:1200px;height:30px;border-top:1px solid #2b303c;font-size:10px;color:#8e93a0;text-align:center;line-height:30px}
</style>
</head>
<body>

<section class="section hero">
  <div class="hero-bg" role="img" aria-label="Industrial plant interior with machinery in blue light"></div>
  <div class="hero-person" role="img" aria-label="Engineer in safety vest and hard hat inspecting equipment"></div>
  <div class="hero-shade"></div>

  <div class="brand"><span class="brand-dot"></span><span class="brand-name">BrightFloe</span></div>
  <div class="brand-tag">Oil Separation &amp; Coolant Recycling</div>

  <div class="contact-pills">
    <span class="pill"><svg viewBox="0 0 24 24"><path fill="#d3202b" d="M6.6 10.8a15 15 0 006.6 6.6l2.2-2.2a1 1 0 011-.25 11.4 11.4 0 003.6.57 1 1 0 011 1V20a1 1 0 01-1 1A17 17 0 013 4a1 1 0 011-1h3.5a1 1 0 011 1c0 1.25.2 2.45.57 3.57a1 1 0 01-.25 1z"/></svg>(555) 441-7390</span>
    <span class="pill"><svg viewBox="0 0 24 24"><path fill="#d3202b" d="M3 5h18v14H3zm2 2v.5l7 4.5 7-4.5V7z"/></svg>sales@brightfloe-example.com</span>
  </div>
  <div class="estimate">Request An<br>Estimate</div>

  <nav class="main-nav">
    <a href="#">Products</a><a href="#">Benefits</a><a href="#" class="current">Industries Served</a><a href="#">About Us</a><a href="#">Service &amp; Support</a>
  </nav>

  <h1 class="hero-title">Oil Separation &amp; Coolant <span>Recycling Systems Experts</span></h1>
  <p class="hero-lead">Clean process fluids, longer coolant life and less waste for CNC shops that need dependable separation every day.</p>
  <div class="hero-actions">
    <a class="btn btn-red" href="#"><svg viewBox="0 0 12 12"><path d="M3 1l5 5-5 5" stroke="#fff" stroke-width="2" fill="none"/></svg>Start Your Project</a>
    <a class="btn btn-navy" href="#"><svg viewBox="0 0 12 12"><path d="M3 1l5 5-5 5" stroke="#fff" stroke-width="2" fill="none"/></svg>Why Choose Us</a>
  </div>

  <svg class="hero-wave" viewBox="0 0 1200 110" preserveAspectRatio="none">
    <path d="M0 60 L600 20 L1200 40 L1200 110 L0 110Z" fill="#d3202b"/>
    <path d="M0 80 L600 40 L1200 70 L1200 110 L0 110Z" fill="#ffffff"/>
  </svg>
</section>

<section class="section about">
  <div class="about-visual" role="img" aria-label="Illustration of coolant and oil droplets"></div>
  <div class="about-text">
    <h2 class="section-title">About Us</h2>
    <p class="body-copy">Since 1980, the BrightFloe product line has been producing some of the best solutions in the world for the management of industrial fluids. Our products combine innovative design, rugged durability and performance in partnership with you. You can rest assured that you have invested in the best. But don't just take our word for it. We have seven separate patents relating to the unique skimming and separation processes that set our products apart.</p>
    <a class="learn" href="#">Learn More <svg viewBox="0 0 12 12"><path d="M2 2l4 4-4 4M6 2l4 4-4 4" stroke="#d3202b" stroke-width="1.6" fill="none"/></svg></a>
  </div>
</section>

<section class="section product tint oil">
  <div class="product-text">
    <h2 class="product-title">Oil Water Separators</h2>
    <p class="body-copy">The BrightFloe "non-clogging" design allows for the separation of oily and settling of solids in one step.</p>
    <a class="learn" href="#">Learn More <svg viewBox="0 0 12 12"><path d="M2 2l4 4-4 4M6 2l4 4-4 4" stroke="#d3202b" stroke-width="1.6" fill="none"/></svg></a>
  </div>
  <div class="product-img" role="img" aria-label="Stainless oil water separator units with hoses"></div>
</section>

<section class="section product coolant">
  <div class="product-img" role="img" aria-label="Blue coolant recycling system on a wheeled frame"></div>
  <div class="product-text">
    <h2 class="product-title">Coolant Recycling Systems</h2>
    <p class="body-copy">The FloeGuard™ Coolant Recycling Systems are based on decades-long successful fluid treatment practices, using the award-winning multipatented BrightFloe™ systems approach to solving problems.</p>
    <a class="learn" href="#">Learn More <svg viewBox="0 0 12 12"><path d="M2 2l4 4-4 4M6 2l4 4-4 4" stroke="#d3202b" stroke-width="1.6" fill="none"/></svg></a>
  </div>
</section>

<section class="section product tint magnetic">
  <div class="product-text">
    <h2 class="product-title">Magnetic Separators</h2>
    <p class="body-copy">BrightFloe magnetic separators fit with our core philosophies, providing products that eliminate the use of filter consumables, are easy to implement, simple to operate, and require minimal maintenance.</p>
    <a class="learn" href="#">Learn More <svg viewBox="0 0 12 12"><path d="M2 2l4 4-4 4M6 2l4 4-4 4" stroke="#d3202b" stroke-width="1.6" fill="none"/></svg></a>
  </div>
  <div class="product-img" role="img" aria-label="Machinist working at a CNC machine, faded"></div>
</section>

<section class="section trusted">
  <h2 class="trusted-title">Trusted By</h2>
  <div class="logo-row">
    <svg class="arrow" viewBox="0 0 22 22"><path d="M14 3L6 11l8 8" stroke="#1d2433" stroke-width="3" fill="none"/></svg>
    <span class="client"><i></i>Harlow Motors</span>
    <span class="client"><i></i>Valtorre</span>
    <span class="client"><i></i>Kessler</span>
    <span class="client"><i></i>Gallwin</span>
    <span class="client"><i></i>Raymark</span>
    <svg class="arrow" viewBox="0 0 22 22"><path d="M8 3l8 8-8 8" stroke="#1d2433" stroke-width="3" fill="none"/></svg>
  </div>
</section>

<section class="section roi">
  <svg class="roi-bands" viewBox="0 0 1200 570" preserveAspectRatio="none">
    <path d="M0 20 L600 60 L1200 10 L1200 60 L600 100 L0 70Z" fill="#d3202b"/>
    <path d="M0 70 L600 100 L1200 60 L1200 540 L0 540Z" fill="#15306b"/>
    <path d="M0 520 L600 545 L1200 505 L1200 550 L600 570 L0 548Z" fill="#d3202b"/>
  </svg>
  <div class="roi-panel" role="img" aria-label="Factory floor with coolant system, blue tinted">
    <div class="roi-heading">Our Roi Calculator</div>
    <div class="slider" style="top:140px">
      <div class="slider-label">Reduction in coolant costs</div>
      <div class="slider-row"><b>50%</b><div class="slider-track"><div class="slider-fill" style="width:55%"></div><div class="slider-knob" style="left:53%"></div></div><b>75%</b></div>
    </div>
    <div class="slider" style="top:250px">
      <div class="slider-label">Reduction in waste removal</div>
      <div class="slider-row"><b>20%</b><div class="slider-track"><div class="slider-fill" style="width:40%"></div><div class="slider-knob" style="left:38%"></div></div><b>80%</b></div>
    </div>
  </div>
  <div class="roi-left">
    <div class="roi-brand"><span class="brand-dot"></span><span class="brand-name" style="font-size:26px">BrightFloe</span></div>
    <p class="roi-copy">By Drastically Reducing Coolant Costs And The Cost Of Waste Removal, Our Typical Systems Pay For Themselves In 6-9 Months. Check Out Our ROI Calculator To Determine How Much You Can Save With Our Coolant Recycling Systems.</p>
    <a class="btn btn-red" href="#"><svg viewBox="0 0 12 12"><path d="M3 1l5 5-5 5" stroke="#fff" stroke-width="2" fill="none"/></svg>Apply Now</a>
  </div>
</section>

<section class="section cases">
  <h2 class="cases-title">Learn How They Did It</h2>
  <div class="case-row">
    <svg class="arrow" viewBox="0 0 22 22"><path d="M14 3L6 11l8 8" stroke="#1d2433" stroke-width="3" fill="none"/></svg>
    <div class="case-card"><p>See how a precision machining shop cut coolant purchases in half and kept sumps clean after installing a BrightFloe system.</p><div class="case-badge"></div><div class="case-lines"><span></span><span style="width:110px"></span></div></div>
    <div class="case-card"><p>See how a precision machining shop cut coolant purchases in half and kept sumps clean after installing a BrightFloe system.</p><div class="case-badge"></div><div class="case-lines"><span></span><span style="width:110px"></span></div></div>
    <div class="case-card"><p>See how a precision machining shop cut coolant purchases in half and kept sumps clean after installing a BrightFloe system.</p><div class="case-badge"></div><div class="case-lines"><span></span><span style="width:110px"></span></div></div>
    <div class="case-card"><p>See how a precision machining shop cut coolant purchases in half and kept sumps clean after installing a BrightFloe system.</p><div class="case-badge"></div><div class="case-lines"><span></span><span style="width:110px"></span></div></div>
    <svg class="arrow" viewBox="0 0 22 22"><path d="M8 3l8 8-8 8" stroke="#1d2433" stroke-width="3" fill="none"/></svg>
  </div>
</section>

<section class="section newsletter" role="img" aria-label="Dark workshop background">
  <h2 class="news-title">Subscribe To Our Newsletter</h2>
  <div class="news-form">
    <span class="field"><svg viewBox="0 0 24 24"><path fill="#8b91a0" d="M3 5h18v14H3zm2 2v.5l7 4.5 7-4.5V7z"/></svg>Enter Your Email</span>
    <span class="submit">Subscribe</span>
  </div>
</section>

<footer class="section footer">
  <div class="footer-brand">
    <div class="brand-row"><span class="brand-dot"></span><span class="brand-name">BrightFloe</span></div>
    <p>Since 1980 the BrightFloe product line has been delivering practical fluid management tools for machine shops worldwide, helping plants save coolant, reduce waste and keep equipment running at its best every day.</p>
  </div>
  <div class="footer-col" style="left:395px">
    <h4>Menu</h4>
    <ul><li>Products</li><li>Benefits</li><li>Industries Served</li><li>About Us</li><li>Service &amp; Support</li></ul>
  </div>
  <div class="footer-col" style="left:560px">
    <h4>Products</h4>
    <ul><li>Oil Water Separators</li><li>Coolant Recycling Systems</li><li>Magnetic Separators</li><li>Floating Suction Skimmers</li><li>Spare Parts</li></ul>
  </div>
  <div class="footer-col" style="left:790px">
    <h4>Contact us</h4>
    <ul>
      <li class="contact-line"><svg viewBox="0 0 24 24"><path fill="#d3202b" d="M6.6 10.8a15 15 0 006.6 6.6l2.2-2.2a1 1 0 011-.25 11.4 11.4 0 003.6.57 1 1 0 011 1V20a1 1 0 01-1 1A17 17 0 013 4a1 1 0 011-1h3.5a1 1 0 011 1c0 1.25.2 2.45.57 3.57a1 1 0 01-.25 1z"/></svg>(555) 441-7390</li>
      <li class="contact-line"><svg viewBox="0 0 24 24"><path fill="#d3202b" d="M3 5h18v14H3zm2 2v.5l7 4.5 7-4.5V7z"/></svg>sales@brightfloe-example.com</li>
    </ul>
  </div>
  <div class="footer-col" style="left:1010px">
    <h4>Follow us</h4>
    <div class="social"><i></i><i></i><i></i><i></i></div>
  </div>
  <div class="copyright">© Copyright 2024 BrightFloe. All Rights Reserved.</div>
</footer>

</body>
</html>
```